ORVET - Helping People with Disabilities

ORVET is a nonprofit that strives to enable people with physical disabilities to live meaningful, quality lives. ORVET needs a professional attractive website that:
• establishes a strong brand image
• presents Orvet's services to those who need it
• raises funds from potential donors
Please see WORD DOC attached for more information about design vision.

Target Market(s)

people with disabilities

Industry/Entity Type

charity website

Number of Pages Required

2 page

Font styles to use
Sans Serif

Requirements
Must have
• 1. 2 pages means 1 design for homepage and 1 design for top of inner pages (banner ideas)
Nice to have
• please see attached design brief (WORD DOC)

```html
<!DOCTYPE html>
<html lang="en">
<head>
<meta charset="utf-8">
<title>ORVET – A Good Life for Everyone</title>
<link href="https://fonts.googleapis.com/css2?family=Exo+2:wght@400;500;600;700&family=Poppins:wght@400;500;600&display=swap" rel="stylesheet">
<style>
:root{
  --teal-dark:#0b6d68;
  --teal-deep:#08605b;
  --green:#3bb54a;
  --red:#d8393c;
  --cyan:#2cc0c3;
  --grey:#666;
  --ink:#222;
  --muted:#555;
  --line:#e6e6e6;
  --white:#fff;
}
*{box-sizing:border-box;margin:0;padding:0}
html,body{width:1200px;height:4474px;overflow:hidden}
body{font-family:"Poppins",sans-serif;color:var(--ink);background:var(--white);position:relative}
.abs{position:absolute}
.heading{font-family:"Exo 2",sans-serif}
.btn{position:absolute;display:flex;align-items:center;justify-content:center;color:#fff;font-size:11px;font-weight:500;border-radius:2px}
.btn.red{background:var(--red)}
.btn.green{background:var(--green)}
.btn.teal{background:var(--teal-dark)}

/* header */
.site-header{position:absolute;left:0;top:0;width:1200px;height:125px;background:#fff}
.brand{position:absolute;left:137px;top:42px;font-family:"Exo 2",sans-serif;font-weight:700;font-size:32px;color:var(--teal-dark);letter-spacing:1px}
.topbar{position:absolute;top:24px;left:506px;display:flex;align-items:center;font-size:11px;color:var(--grey);gap:16px}
.topbar .call{color:var(--green);font-size:13px;font-weight:500}
.topbar .call b{color:var(--teal-dark);font-weight:600;margin-left:6px}
.topbar .sep{color:#bbb}
.socials{display:flex;gap:8px}
.social{width:30px;height:30px;border-radius:50%;background:var(--cyan)}
.lang{width:32px;height:32px;border-radius:50%;border:1px solid #999;display:flex;align-items:center;justify-content:center;font-size:9px;font-weight:600;margin-left:18px}
.main-nav{position:absolute;top:76px;left:294px;display:flex;gap:27px;font-size:11px;font-weight:500}
.main-nav .active{color:var(--red)}

/* hero */
.hero{position:absolute;left:0;top:125px;width:1200px;height:436px;background:linear-gradient(100deg,#4d6a3a 0%,#7a8f55 35%,#a79a6d 55%,#5e7a40 80%,#3f5a30 100%)}
.hero-shade{position:absolute;inset:0;background:rgba(0,0,0,.18)}
.hero h1{position:absolute;top:130px;width:1200px;text-align:center;font-family:"Exo 2",sans-serif;font-weight:600;font-size:46px;line-height:54px;color:#fff}

/* know card */
.know{position:absolute;left:200px;top:528px;width:800px;height:537px;background:#fff;box-shadow:0 2px 14px rgba(0,0,0,.1)}
.know h2{position:absolute;top:32px;width:800px;text-align:center;font-family:"Exo 2",sans-serif;font-weight:500;font-size:20px;color:var(--teal-dark)}
.acc{position:absolute;left:31px;width:738px;height:49px;color:#fff;font-size:12px;display:flex;align-items:center;padding-left:75px}
.acc .ico{position:absolute;left:20px;top:10px;width:30px;height:30px}
.acc .plus{position:absolute;right:22px;top:18px;width:13px;height:13px;border:1.4px solid #fff;border-radius:50%}
.acc .plus::before,.acc .plus::after{content:"";position:absolute;background:#fff;left:3px;top:5px;width:5px;height:1.2px}
.acc .plus::after{transform:rotate(90deg)}
.acc-text{position:absolute;left:55px;top:243px;width:690px;font-size:10.5px;line-height:19px;color:var(--muted)}

/* about */
.eyebrow{font-family:"Exo 2",sans-serif;font-weight:500;font-size:15px;color:var(--green)}
.section-title{font-family:"Exo 2",sans-serif;font-weight:600;font-size:31px;color:var(--teal-dark)}
.about-text{position:absolute;left:200px;width:390px;font-size:10.5px;line-height:19px;color:var(--ink)}

/* services */
.services{position:absolute;left:0;top:1618px;width:1200px;height:593px;background:var(--teal-dark);color:#fff}
.service{position:absolute;top:169px;width:195px}
.service .photo{height:156px}
.service h3{margin-top:31px;font-family:"Exo 2",sans-serif;font-weight:500;font-size:15px;line-height:18px}
.service p{margin-top:20px;font-size:10px;line-height:19px;color:#e6f1f0}
.service .more{position:absolute;top:331px;font-size:10px;font-weight:600}
.divider{position:absolute;top:169px;width:1px;height:370px;background:rgba(255,255,255,.25)}

/* cta */
.cta{position:absolute;left:0;top:2211px;width:1200px;height:283px;background:linear-gradient(90deg,#2bbec1,#35c6c9 50%,#2bbec1)}
.cta h2{position:absolute;top:64px;width:1200px;text-align:center;font-family:"Exo 2",sans-serif;font-weight:600;font-size:37px;line-height:46px;color:#fff}

/* branches */
.branches{position:absolute;left:0;top:2494px;width:1200px;height:523px;background:linear-gradient(180deg,#fff,#f3f3f3)}
.branch{position:absolute;font-size:11px;font-weight:500;display:flex;align-items:center;gap:14px}
.pin{width:9px;height:12px}
.frame{position:absolute;left:613px;top:2570px;width:387px;height:374px;border:2px solid var(--green);background:#fff}

/* news */
.news-card{position:absolute;top:3171px;width:250px;height:363px;background:#fff;box-shadow:0 2px 12px rgba(0,0,0,.07)}
.news-card .photo{height:169px}
.news-card h3{margin:26px 18px 0;font-family:"Exo 2",sans-serif;font-weight:500;font-size:15px;line-height:19px;color:var(--green)}
.news-card p{margin:18px 18px 0;font-size:10px;line-height:19px;color:var(--ink)}
.news-card .more{position:absolute;left:18px;top:326px;font-size:10.5px;font-weight:600;color:var(--teal-dark)}

/* quote */
.footer{position:absolute;left:0;top:3911px;width:1200px;height:563px;background:var(--teal-dark);color:#fff}
.quote{position:absolute;left:262px;top:3668px;width:676px;height:411px;background:var(--green);color:#fff}
.field{position:absolute;background:#fff;border:1px solid #cfcfcf;font-size:9px;color:#777;padding:10px 18px}
.foot-h{position:absolute;font-family:"Exo 2",sans-serif;font-size:14px;color:var(--green);font-weight:500}
.foot-row{position:absolute;font-size:11px;display:flex;gap:12px;align-items:flex-start}
.foot-link{position:absolute;font-size:10.5px}
</style>
</head>
<body>

<header class="site-header">
  <div class="brand">ORVET</div>
  <div class="topbar">
    <span class="call">Call Us Today <b>03-5550172</b></span>
    <span class="sep">|</span><span>Shop</span><span class="sep">|</span><span>Joining ORVET</span>
    <div class="socials" style="margin-left:18px"><span class="social"></span><span class="social"></span><span class="social"></span></div>
    <span class="lang">EN</span>
  </div>
  <nav class="main-nav">
    <span class="active">- Home -</span><span>About</span><span>Programs</span><span>Rehabilitation &amp; Sports</span><span>Rights Realization</span><span>News</span><span>Contact Us</span>
  </nav>
  <span class="btn red" style="left:938px;top:66px;width:123px;height:38px">Donation to Orvet</span>
</header>

<section class="hero" role="img" aria-label="Photo of a girl in a wheelchair reaching for a basketball outdoors">
  <div class="hero-shade"></div>
  <h1>A Good Life for Everyone,<br>Like Everyone</h1>
  <span class="btn red" style="left:491px;top:274px;width:218px;height:37px">Donate to Help Us Help Them</span>
</section>

<section class="know">
  <h2>I Want to Know:</h2>
  <svg class="abs" style="left:395px;top:70px" width="10" height="6" viewBox="0 0 10 6"><path d="M1 1l4 4 4-4" fill="none" stroke="#0b6d68" stroke-width="1.4"/></svg>

  <div class="acc" style="top:113px;background:var(--teal-dark)">
    <svg class="ico" viewBox="0 0 30 30" fill="none" stroke="#fff" stroke-width="1.8"><circle cx="14" cy="5" r="3"/><path d="M14 9v9h8l3 7"/><path d="M11 13a8 8 0 1 0 9 11"/></svg>
    What are all the rights available to people with physical disabilities and their families?<span class="plus"></span></div>
  <div class="acc" style="top:175px;background:var(--green);box-shadow:0 4px 10px rgba(0,0,0,.15)">
    <svg class="ico" viewBox="0 0 30 30" fill="none" stroke="#fff" stroke-width="1.8"><path d="M7 2h12l5 5v21H7z"/><path d="M13 12l7 4-7 4z"/></svg>
    Where I can join online classes offered by ORVET?<span class="plus"></span></div>
  <p class="acc-text">Lorem Ipsum is simply dummy text of the printing and typesetting industry. Lorem Ipsum has been the industry's standard dummy text ever since the 1500s, when an unknown printer took a galley of type and scrambled it to make a type specimen book. It has survived not only five centuries, but also the leap into electronic typesetting, remaining essentially unchanged.</p>
  <div class="acc" style="top:325px;background:var(--cyan)">
    <svg class="ico" viewBox="0 0 30 30" fill="none" stroke="#fff" stroke-width="1.8"><circle cx="17" cy="5" r="3"/><path d="M16 9l-4 8h7l2 8"/><circle cx="9" cy="23" r="5"/></svg>
    What services there are for children with disabilities?<span class="plus"></span></div>
  <div class="acc" style="top:387px;background:var(--grey)">
    <svg class="ico" viewBox="0 0 30 30" fill="none" stroke="#fff" stroke-width="1.8"><path d="M6 4h18v24H6z"/><path d="M15 8v6M12 11h6M10 18h3M17 18h3M10 23h3M17 23h3"/></svg>
    If there is a rehabilitation center in my area?<span class="plus"></span></div>
  <span class="btn green" style="left:338px;top:469px;width:125px;height:38px">Donation to Orvet</span>
</section>

<section>
  <div class="abs eyebrow" style="left:200px;top:1195px">Who we are</div>
  <div class="abs section-title" style="left:200px;top:1225px">What is the Orvet association?</div>
  <p class="about-text" style="top:1290px">The Orvet association is one of the oldest associations in the country, which works to create support systems to integrate children and adults with disabilities, as independent and equal members of the wider society. In its vision, Orvet believes in providing a meaningful and high-quality life to people with physical disabilities</p>
  <p class="about-text" style="top:1404px">The association was founded in 1961 by volunteers who wanted to support families in need. Since then, the association's activities have expanded and today, the association operates activity frameworks under contracts with the national welfare authorities ...</p>
  <span class="btn green" style="left:201px;top:1507px;width:113px;height:35px">Explore More</span>
  <svg class="abs" style="left:611px;top:1141px" width="389" height="372" viewBox="0 0 389 372" role="img" aria-label="Photo of a smiling man in a wheelchair by the sea, framed in a triangle">
    <defs><linearGradient id="sea" x1="0" y1="0" x2="0" y2="1"><stop offset="0" stop-color="#c9dde6"/><stop offset=".5" stop-color="#8fa9b3"/><stop offset="1" stop-color="#7d7b78"/></linearGradient></defs>
    <polygon points="194,0 389,328 360,328 194,48 30,372 0,372" fill="#0b6d68"/>
    <polygon points="194,48 360,328 380,372 30,372" fill="url(#sea)"/>
  </svg>
</section>

<section class="services">
  <div class="abs heading" style="top:72px;width:1200px;text-align:center;font-size:14px;font-weight:500">Our Services</div>
  <div class="abs heading" style="top:102px;width:1200px;text-align:center;font-size:31px;font-weight:500">What we offer you</div>
  <div class="service" style="left:137px"><div class="photo" role="img" aria-label="Photo of children drawing together at a table" style="background:linear-gradient(135deg,#c99f80,#8f6f5c)"></div><h3>Education<br>Orvet</h3><p>Works to impart education and knowledge to people with disabili-ties and operates the dedicated campus ...</p><span class="more">Read More →</span></div>
  <div class="divider" style="left:356px"></div>
  <div class="service" style="left:380px"><div class="photo" role="img" aria-label="Photo of a woman stretching in a bright gym" style="background:linear-gradient(135deg,#e8e8e8,#9aa3ad)"></div><h3>Sports and Rehab<br>Orvet</h3><p>Encourages people with disabilities to play sports and find new strengths in themselves...</p><span class="more" style="color:var(--green)">Read More →</span></div>
  <div class="divider" style="left:599px"></div>
  <div class="service" style="left:623px"><div class="photo" role="img" aria-label="Photo of a judge's gavel and scales of justice" style="background:linear-gradient(135deg,#5a4b3d,#2a2520)"></div><h3>Rights Realization<br>Orvet</h3><p>Promotes policies concerning people with physical-motor disabilities, promotes their rights, ...</p><span class="more">Read More →</span></div>
  <div class="divider" style="left:844px"></div>
  <div class="service" style="left:868px"><div class="photo" role="img" aria-label="Photo of volunteers sorting donation boxes" style="background:linear-gradient(135deg,#d9cdb8,#6f6a62)"></div><h3>Community Infrastructure<br>Orvet</h3><p>Owns the association's houses all over the country, rehabilitation day centers,...</p><span class="more">Read More →</span></div>
</section>

<section class="cta" role="img" aria-label="Faint photo of a person in a wheelchair under a teal tint">
  <h2>Even people with disabilities can be<br>with everyone, like everyone</h2>
  <span class="btn red" style="left:497px;top:179px;width:206px;height:36px">Don't Leave Them Behind</span>
</section>

<section class="branches">
  <div class="abs eyebrow" style="left:200px;top:117px;font-size:14px">Orvet</div>
  <div class="abs section-title" style="left:200px;top:136px">Branch list</div>
</section>
<div class="branch" style="left:200px;top:2700px"><svg class="pin" viewBox="0 0 9 12"><path d="M4.5 0a4.5 4.5 0 0 0-4.5 4.5C0 8 4.5 12 4.5 12S9 8 9 4.5A4.5 4.5 0 0 0 4.5 0z" fill="#3bb54a"/><circle cx="4.5" cy="4.5" r="1.6" fill="#fff"/></svg>Northfield Vale</div>
<div class="branch" style="left:200px;top:2728px"><svg class="pin" viewBox="0 0 9 12"><path d="M4.5 0a4.5 4.5 0 0 0-4.5 4.5C0 8 4.5 12 4.5 12S9 8 9 4.5A4.5 4.5 0 0 0 4.5 0z" fill="#3bb54a"/><circle cx="4.5" cy="4.5" r="1.6" fill="#fff"/></svg>Lakeside</div>
<div class="branch" style="left:200px;top:2758px"><svg class="pin" viewBox="0 0 9 12"><path d="M4.5 0a4.5 4.5 0 0 0-4.5 4.5C0 8 4.5 12 4.5 12S9 8 9 4.5A4.5 4.5 0 0 0 4.5 0z" fill="#3bb54a"/><circle cx="4.5" cy="4.5" r="1.6" fill="#fff"/></svg>Harbor Bay</div>
<div class="branch" style="left:200px;top:2787px"><svg class="pin" viewBox="0 0 9 12"><path d="M4.5 0a4.5 4.5 0 0 0-4.5 4.5C0 8 4.5 12 4.5 12S9 8 9 4.5A4.5 4.5 0 0 0 4.5 0z" fill="#3bb54a"/><circle cx="4.5" cy="4.5" r="1.6" fill="#fff"/></svg>Westmoor</div>
<div class="branch" style="left:200px;top:2815px"><svg class="pin" viewBox="0 0 9 12"><path d="M4.5 0a4.5 4.5 0 0 0-4.5 4.5C0 8 4.5 12 4.5 12S9 8 9 4.5A4.5 4.5 0 0 0 4.5 0z" fill="#3bb54a"/><circle cx="4.5" cy="4.5" r="1.6" fill="#fff"/></svg>Southridge</div>
<div class="branch" style="left:358px;top:2700px"><svg class="pin" viewBox="0 0 9 12"><path d="M4.5 0a4.5 4.5 0 0 0-4.5 4.5C0 8 4.5 12 4.5 12S9 8 9 4.5A4.5 4.5 0 0 0 4.5 0z" fill="#3bb54a"/><circle cx="4.5" cy="4.5" r="1.6" fill="#fff"/></svg>Eastvale</div>
<div class="branch" style="left:358px;top:2728px"><svg class="pin" viewBox="0 0 9 12"><path d="M4.5 0a4.5 4.5 0 0 0-4.5 4.5C0 8 4.5 12 4.5 12S9 8 9 4.5A4.5 4.5 0 0 0 4.5 0z" fill="#3bb54a"/><circle cx="4.5" cy="4.5" r="1.6" fill="#fff"/></svg>Hillcrest</div>
<div class="branch" style="left:358px;top:2758px"><svg class="pin" viewBox="0 0 9 12"><path d="M4.5 0a4.5 4.5 0 0 0-4.5 4.5C0 8 4.5 12 4.5 12S9 8 9 4.5A4.5 4.5 0 0 0 4.5 0z" fill="#3bb54a"/><circle cx="4.5" cy="4.5" r="1.6" fill="#fff"/></svg>Brookton - Glenport</div>
<div class="branch" style="left:358px;top:2787px"><svg class="pin" viewBox="0 0 9 12"><path d="M4.5 0a4.5 4.5 0 0 0-4.5 4.5C0 8 4.5 12 4.5 12S9 8 9 4.5A4.5 4.5 0 0 0 4.5 0z" fill="#3bb54a"/><circle cx="4.5" cy="4.5" r="1.6" fill="#fff"/></svg>Fairhaven</div>
<div class="branch" style="left:358px;top:2815px"><svg class="pin" viewBox="0 0 9 12"><path d="M4.5 0a4.5 4.5 0 0 0-4.5 4.5C0 8 4.5 12 4.5 12S9 8 9 4.5A4.5 4.5 0 0 0 4.5 0z" fill="#3bb54a"/><circle cx="4.5" cy="4.5" r="1.6" fill="#fff"/></svg>Oakmont</div>
<span class="btn green" style="left:200px;top:2865px;width:111px;height:34px">View All</span>
<div class="frame"><div class="abs" role="img" aria-label="Photo of smiling volunteers in blue shirts holding a donation box" style="left:10px;top:10px;width:363px;height:350px;background:linear-gradient(150deg,#9fb9c7,#5f97c4 55%,#7fb24a)"></div></div>

<section>
  <div class="abs heading" style="top:3090px;width:1200px;text-align:center;font-size:15px;font-weight:500;color:var(--green)">Recent News</div>
  <div class="abs section-title" style="top:3114px;width:1200px;text-align:center">Latest articles</div>
  <article class="news-card" style="left:200px"><div class="photo" role="img" aria-label="Photo of a group hiking on a dirt trail" style="background:linear-gradient(160deg,#b9c3b0,#8b7b63)"></div><h3>Lorem Ipsum is simply dummy text of the printing</h3><p>Lorem Ipsum has been the industry's standard dummy text ever since the 1500s, printer took a galley ...</p><span class="more">Read More →</span></article>
  <article class="news-card" style="left:476px"><div class="photo" role="img" aria-label="Photo of people in wheelchairs at an indoor event" style="background:linear-gradient(160deg,#6b6b7a,#b8c26a 60%,#4b4b55)"></div><h3>Lorem Ipsum is simply dummy text of the printing</h3><p>Lorem Ipsum has been the industry's standard dummy text ever since the 1500s, printer took a galley ...</p><span class="more">Read More →</span></article>
  <article class="news-card" style="left:750px"><div class="photo" role="img" aria-label="Photo of a beach wheelchair at the seashore" style="background:linear-gradient(180deg,#a9c8df,#d9c9a3 65%,#c9b48a)"></div><h3>Lorem Ipsum is simply dummy text of the printing</h3><p>Lorem Ipsum has been the industry's standard dummy text ever since the 1500s, printer took a galley ...</p><span class="more">Read More →</span></article>
  <span class="btn red" style="left:544px;top:3569px;width:112px;height:36px">View All</span>
</section>

<footer class="footer">
  <div class="abs heading" style="left:200px;top:295px;font-size:36px;font-weight:700;color:#fff;letter-spacing:1px">ORVET</div>
  <div class="foot-h" style="left:387px;top:245px">Contact Us</div>
  <div class="foot-row" style="left:387px;top:281px;font-size:13px;font-weight:500"><svg width="11" height="11" viewBox="0 0 12 12"><path d="M3 1l2 3-1.5 1.5a7 7 0 0 0 3 3L8 7l3 2-1 2C5 11 1 7 1 2z" fill="#3bb54a"/></svg>03-5550172</div>
  <div class="foot-row" style="left:387px;top:310px;font-size:13px;font-weight:500"><svg width="11" height="11" viewBox="0 0 12 12"><path d="M3 1l2 3-1.5 1.5a7 7 0 0 0 3 3L8 7l3 2-1 2C5 11 1 7 1 2z" fill="#3bb54a"/></svg>03-5550173</div>
  <div class="foot-row" style="left:387px;top:342px;font-size:10.5px"><svg width="11" height="9" viewBox="0 0 11 9"><rect x=".5" y=".5" width="10" height="8" fill="none" stroke="#3bb54a"/><path d="M.5.5l5 4 5-4" fill="none" stroke="#3bb54a"/></svg>info@orvet-mail.org</div>
  <div class="foot-row" style="left:387px;top:372px;font-size:10.5px;line-height:19px"><svg width="9" height="12" viewBox="0 0 9 12"><path d="M4.5 0a4.5 4.5 0 0 0-4.5 4.5C0 8 4.5 12 4.5 12S9 8 9 4.5A4.5 4.5 0 0 0 4.5 0z" fill="#3bb54a"/></svg><span>12 Cedar Lane, P.O.<br>Box 410<br>Riverton 1000200</span></div>
  <div class="foot-h" style="left:601px;top:245px">Quick Links</div>
  <span class="foot-link" style="left:601px;top:283px">Home</span>
  <span class="foot-link" style="left:601px;top:306px">About</span>
  <span class="foot-link" style="left:601px;top:328px">Programs</span>
  <span class="foot-link" style="left:601px;top:351px">Rehabilitation &amp; Sports</span>
  <span class="foot-link" style="left:601px;top:374px">Rights Realization</span>
  <span class="foot-link" style="left:601px;top:396px">News</span>
  <span class="foot-link" style="left:601px;top:419px">Contact Us</span>
  <span class="foot-link" style="left:735px;top:283px">Term &amp; Conditions</span>
  <span class="foot-link" style="left:735px;top:306px">Privacy Policy</span>
  <div class="foot-h" style="left:893px;top:245px">Follow Us</div>
  <div class="socials abs" style="left:893px;top:280px"><span class="social"></span><span class="social" style="background:var(--red)"></span><span class="social"></span></div>
  <div class="abs" style="left:200px;top:487px;font-size:10.5px">© 2023 <b style="font-weight:600">Orvet Association.</b> All Right Reserved &nbsp;&nbsp;|&nbsp;&nbsp; Accessibility Statement</div>
  <svg class="abs" style="left:1125px;top:486px" width="16" height="16" viewBox="0 0 16 16"><path d="M8 1l7 14-7-4-7 4z" fill="#3bb54a"/></svg>
</footer>

<section class="quote">
  <div class="abs heading" style="top:46px;width:676px;text-align:center;font-size:14px;font-weight:500">Get In Touch</div>
  <div class="abs heading" style="top:70px;width:676px;text-align:center;font-size:30px;font-weight:500">Get a free quote</div>
  <div class="field" style="left:82px;top:130px;width:248px;height:36px">Name</div>
  <div class="field" style="left:344px;top:130px;width:250px;height:36px">Phone</div>
  <div class="field" style="left:82px;top:180px;width:512px;height:37px">Email Address</div>
  <div class="field" style="left:82px;top:229px;width:512px;height:68px">Message...</div>
  <span class="btn teal" style="left:282px;top:312px;width:112px;height:37px">Submit</span>
</section>

</body>
</html>
```